High value cover design for an A4 ideation pad.

The product is NOT A BOOK.

It's an A4 ideation pad for professionals, designers and creators who handwrite their ideas. Visualise creators like Paul Menteith, Glen Usborne and Carl Whitmoor in your mind's eye.

I'm looking for a cover design for the ideation pad. Both front and back.

It should look, feel and convey the following.

--> A handcrafted product experience

--> High value & Elegance

--> Inspiration

Mandatory --> See Uploaded Files --> Files 1, 5 & 6

Target Market(s)

- Designers

-Creative Professionals

- Entrepreneurs

who handwrite their ideas. Visualise creators like Paul Menteith, Glen Usborne and Carl Whitmoor in your mind's eye.

Industry/Entity Type

Stationary

Font styles to use
Script
Other font styles liked:
• Calligraphy

Colors
fbed22

Requirements
Must have
• Title text - Ink And Iron

-Text in gold on brown leather background to convey high value for the front cover.

--> High value & Elegance

--> Inspiration

--> Should compel the customers to pick up and own the idea pad
Nice to have
• That's my take but other ideas are welcome
Should not have
• Must not convey

- low value

```html
<!DOCTYPE html>
<html lang="en">
<head>
<meta charset="utf-8">
<title>Ink And Iron – Ideation Pad Cover</title>
<link href="https://fonts.googleapis.com/css2?family=Great+Vibes&family=Cinzel:wght@400&display=swap" rel="stylesheet">
<style>
  :root {
    --backdrop: #c68a52;
    --cover-black: #221f20;
    --gold: #c9a04f;
    --gold-light: #e8cf8e;
    --gold-deep: #9c7536;
  }
  html, body {
    margin: 0;
    padding: 0;
    width: 1200px;
    height: 932px;
    overflow: hidden;
    background: var(--backdrop);
  }
  .spread {
    position: relative;
    width: 1200px;
    height: 932px;
  }
  .cover {
    position: absolute;
    top: 62px;
    width: 557px;
    height: 786px;
    background: var(--cover-black);
    overflow: hidden;
  }
  .cover--back { left: 26px; }
  .cover--front { left: 618px; }

  .corner-mark {
    position: absolute;
    left: 0;
    top: 4px;
    width: 182px;
    height: 152px;
    background: linear-gradient(135deg, var(--gold-light), var(--gold-deep));
    opacity: 0.85;
    clip-path: polygon(0 100%, 100% 0, 100% 12%, 12% 100%);
  }

  .title {
    position: absolute;
    left: 0;
    top: 0;
    width: 557px;
    height: 786px;
    color: var(--gold);
  }
  .title__word {
    position: absolute;
    font-family: "Great Vibes", cursive;
    font-weight: 400;
    line-height: 1;
    white-space: nowrap;
    color: var(--gold);
  }
  .title__word--first {
    left: 140px;
    top: 448px;
    font-size: 150px;
  }
  .title__word--last {
    left: 86px;
    top: 600px;
    font-size: 150px;
  }
  .title__joiner {
    position: absolute;
    left: 262px;
    top: 614px;
    font-family: "Cinzel", serif;
    font-size: 22px;
    letter-spacing: 1px;
    color: var(--gold);
  }
  .title__swash {
    position: absolute;
    left: 0;
    top: 0;
  }
</style>
</head>
<body>
  <main class="spread">
    <section class="cover cover--back" aria-label="Back cover">
      <div class="corner-mark" role="img" aria-label="Gold script initial flourish in the corner"></div>
    </section>

    <section class="cover cover--front" aria-label="Front cover">
      <h1 class="title" aria-label="Ink And Iron">
        <svg class="title__swash" width="557" height="786" viewBox="0 0 557 786" aria-hidden="true">
          <path d="M150 720 C 260 712, 380 690, 440 640" fill="none" stroke="var(--gold)" stroke-width="1.5" stroke-linecap="round"/>
        </svg>
        <span class="title__word title__word--first">Ink</span>
        <span class="title__joiner">AND</span>
        <span class="title__word title__word--last">Iron</span>
      </h1>
    </section>
  </main>
</body>
</html>
```